Halvorsen Construction Needs a Business Card

Our current business card is very bland, and since we have a new logo, we would like a new business card design to reflect our company. It can be a single-sided or two-sided card, but it is important that our contact information appears on the same side. I am attaching a copy of our old card and our new logo. If you need the logo in another format than the one I'm sending, please let me know. This is the information that we must have on our card, but not necessarily in any specific order:
1) Our logo
2) General Contractor
3) Dale Halvorsen, Owner
4) 482 Commerce Ridge Road, Centre, Alabama 35871
5) Office: 256-555-0147
7) Fax: 256-555-0148
8) Cell: 256-555-0193
9) halvorsenconstruction@qvl-mail.net
10) halvorsenconstruction-example.com (can be omitted if necessary)
Also, I will need files in a format that I can alter if any of the above information changes in the near future. Thank you in advance for your submissions!
Target Market(s)
Commercial and residential clients, architects, and subcontractors.
Industry/Entity Type
Business
Look and feel

```html
<!DOCTYPE html>
<html lang="en">
<head>
<meta charset="utf-8">
<title>Halvorsen Construction – Business Card</title>
<link rel="stylesheet" href="https://fonts.googleapis.com/css2?family=Roboto:wght@400;500&display=swap">
<style>
  :root {
    --backdrop: #e4e5e7;
    --panel-dark: #231f20;
    --orange-light: #f7941d;
    --orange-deep: #d9651a;
    --ink: #1c1a1a;
    --paper: #ffffff;
  }
  html, body {
    margin: 0;
    width: 1200px;
    height: 800px;
    overflow: hidden;
    background: var(--backdrop);
    font-family: "Roboto", Arial, sans-serif;
  }
  .stage {
    width: 1200px;
    height: 800px;
    display: flex;
    align-items: center;
    justify-content: center;
  }
  .business-card {
    position: relative;
    width: 1050px;
    height: 600px;
    display: flex;
    box-shadow: 0 10px 30px rgba(0,0,0,0.18);
  }
  .contact-panel {
    width: 420px;
    background: var(--panel-dark);
    color: var(--paper);
    display: flex;
    flex-direction: column;
    justify-content: flex-end;
    padding: 0 24px 70px 48px;
    box-sizing: border-box;
  }
  .role {
    font-size: 16px;
    font-weight: 500;
    letter-spacing: 0.3px;
    text-transform: uppercase;
    margin: 0;
  }
  .owner-name {
    font-size: 28px;
    font-weight: 400;
    margin: 2px 0 20px;
    white-space: nowrap;
  }
  .contact-lines {
    font-size: 13px;
    line-height: 1.55;
    margin: 0;
    font-style: normal;
    white-space: nowrap;
  }
  .brand-panel {
    flex: 1;
    background: radial-gradient(ellipse at 45% 40%, var(--orange-light) 0%, var(--orange-deep) 100%);
    display: flex;
    align-items: center;
    justify-content: center;
    padding-top: 40px;
    box-sizing: border-box;
  }
  .company-name {
    margin: 0;
    color: var(--ink);
    font-size: 38px;
    font-weight: 500;
    white-space: nowrap;
  }
</style>
</head>
<body>
  <main class="stage">
    <section class="business-card">
      <div class="contact-panel">
        <p class="role">General Contractor</p>
        <p class="owner-name">Dale Halvorsen, Owner</p>
        <address class="contact-lines">
          482 Commerce Ridge Road, Centre, Alabama 35871<br>
          Cell : 256-555-0193 | Fax : 256-555-0148<br>
          halvorsenconstruction@qvl-mail.net<br>
          Office : 256-555-0147
        </address>
      </div>
      <div class="brand-panel">
        <p class="company-name">Halvorsen Construction</p>
      </div>
    </section>
  </main>
</body>
</html>
```